1 Home page redesign for existing repair service site.

We need a refresh of our existing website that looks more 2017. We have made a mockup of the content that we want and a sample of where we want it. Nothing is set in stone, if you have better ideas of where things should go, feel free.

You can see our current site at http://www.fixoloda.gr

The colors should stay orange/black/grey.

In many of the "boxes/banners" we will need images. Feel free to find in pixel vault as we have an account.

We have made notes throughout the wireframe that we have attached on what we are looking for. Let us know if you have any questions. Thanks.

Target Market(s)

People using technology and breaking it

Industry/Entity Type

It Service

Number of Pages Required

1 page

Font styles to use
Sans Serif

Requirements
Must have
• Must have a modern, professional look and feel. Need custom graphics and icons.

```html
<!DOCTYPE html>
<html lang="en">
<head>
<meta charset="utf-8">
<title>Fixoloda — Home</title>
<link rel="stylesheet" href="https://fonts.googleapis.com/css2?family=Roboto:wght@300;400;500;700&family=Roboto+Condensed:wght@400;700&display=swap">
<style>
:root{
  --orange:#f07d1c;
  --orange-light:#f49a3c;
  --orange-dark:#e06a0f;
  --ink:#222;
  --text:#555;
  --muted:#888;
  --grey-bg:#f0f0f0;
  --line:#ddd;
  --topbar:#151515;
  --footer:#27313b;
  --footer-line:#3a4653;
  --white:#fff;
}
*{box-sizing:border-box;margin:0;padding:0}
html,body{width:1200px;height:3629px;overflow:hidden;background:var(--white)}
body{position:relative;font-family:"Roboto",Arial,sans-serif;color:var(--text)}
.abs{position:absolute}
.photo{position:absolute;overflow:hidden}

/* top bar */
.topbar{left:0;top:0;width:1200px;height:34px;background:var(--topbar)}
.quick-links{left:160px;top:6px;width:152px;height:22px;border:1px solid #555;color:#fff;font:700 11px "Roboto",sans-serif;letter-spacing:1px;display:flex;align-items:center;justify-content:center;gap:8px}
.quick-links i{display:block;width:0;height:0;border-left:4px solid transparent;border-right:4px solid transparent;border-top:5px solid #fff}
.lang{left:758px;top:9px;color:#bbb;font-size:12px;word-spacing:10px}
.social{left:860px;top:9px;display:flex;gap:12px}
.social span{display:block;width:15px;height:15px;border-radius:50%;background:#8a8a8a}

/* header */
.header{left:0;top:34px;width:1200px;height:78px;background:var(--white);border-bottom:1px solid var(--line)}
.brand{left:160px;top:22px;display:flex;align-items:center;gap:10px;font:700 30px "Roboto",sans-serif;color:var(--ink)}
.brand span{width:32px;height:32px;background:var(--orange);border-radius:4px}
.nav{left:382px;top:0;height:78px;display:flex}
.nav a{display:flex;align-items:center;padding:0 26px;height:78px;border-left:1px solid var(--line);font-size:16px;color:var(--ink);text-decoration:none}
.nav a:last-child{border-right:1px solid var(--line)}
.call{left:760px;top:18px;display:flex;align-items:center;gap:10px}
.call small{display:block;color:var(--orange);font-size:14px}
.call strong{display:block;font:700 24px "Roboto",sans-serif;color:var(--ink);line-height:1}
.livechat{left:952px;top:20px;width:88px;height:42px;border:2px solid var(--ink);border-radius:6px;font:700 15px "Roboto",sans-serif;color:var(--ink);display:flex;align-items:center;justify-content:center}

/* hero */
.hero{left:0;top:112px;width:1200px;height:440px;background:linear-gradient(180deg,#3e3b38,#2a2826 60%,#403a34)}
.play{left:565px;top:180px}
.result-band{left:0;top:552px;width:1200px;height:102px;background:var(--orange)}
.result-band h2{position:absolute;left:430px;top:16px;font:400 31px "Roboto",sans-serif;color:#fff}
.result-band p{position:absolute;left:515px;top:56px;font:300 24px "Roboto",sans-serif;color:#fff}
.counter{left:160px;top:470px;width:236px;height:86px;background:#3b3b3b;border-radius:6px;display:flex;gap:6px;padding:10px;justify-content:center}
.counter span{width:48px;height:66px;background:#1c1c1c;color:#fff;font:700 46px "Roboto Condensed",sans-serif;display:flex;align-items:center;justify-content:center;border-radius:3px}
.counter-label{left:160px;top:556px;width:236px;height:50px}
.counter-label div{position:absolute;left:0;top:6px;width:236px;text-align:center;font:500 13px "Roboto",sans-serif;color:#333;letter-spacing:.5px}

/* promo panels */
.locations{left:0;top:654px;width:557px;height:338px;background:linear-gradient(135deg,#9a9a9a,#c9c9c9 50%,#8c8c8c)}
.locations h3{position:absolute;left:0;width:557px;top:66px;text-align:center;font:300 34px "Roboto",sans-serif;color:#333}
.find-btn{position:absolute;left:180px;top:120px;width:340px;height:72px;background:var(--white);border:3px solid var(--orange);display:flex;align-items:center}
.find-btn b{width:60px;height:66px;background:var(--orange);display:flex;align-items:center;justify-content:center}
.find-btn span{flex:1;text-align:center;font:400 25px "Roboto",sans-serif;color:var(--orange)}
.view-map{position:absolute;left:293px;top:214px;width:120px;height:34px;border-radius:4px;background:#333;color:#fff;font-size:13px;display:flex;align-items:center;justify-content:center;gap:6px}
.view-map i{width:8px;height:8px;border-radius:50%;background:#fff}
.match{left:562px;top:654px;width:638px;height:338px;background:linear-gradient(135deg,#4f6b52,#2f3e36 55%,#587a5a)}
.match h3{position:absolute;left:0;width:638px;top:62px;text-align:center;font:700 28px "Roboto Condensed",sans-serif;color:#fff}
.match h4{position:absolute;left:0;width:638px;top:98px;text-align:center;font:300 28px "Roboto",sans-serif;color:#fff}
.match-box{position:absolute;left:164px;top:152px;width:310px;height:56px;border:2px solid #fff;color:#fff;font:700 29px "Roboto Condensed",sans-serif;display:flex;align-items:center;justify-content:center}
.match small{position:absolute;left:0;width:638px;top:222px;text-align:center;font-size:13px;color:#fff}

/* features */
.feature{top:1048px;width:220px}
.feature .photo{position:relative;width:220px;height:145px;border-bottom:4px solid var(--orange-light)}
.feature h5{margin-top:18px;text-align:center;font:400 17px "Roboto",sans-serif;color:var(--orange);line-height:1.1}
.feature p{margin:10px 18px 0;text-align:center;font-size:11px;line-height:1.5;color:#444;height:34px}
.btn-more{display:flex;margin:16px auto 0;width:96px;height:26px;border:1px solid var(--orange);border-radius:3px;font-size:11px;color:#333;align-items:center;justify-content:center;gap:4px}
.btn-more i{width:7px;height:7px;border-radius:50%;background:var(--orange)}

/* repair grid */
.section-band{left:0;top:1387px;width:1200px;height:70px;background:var(--orange);color:#fff;font:300 36px "Roboto",sans-serif;text-align:center;line-height:70px}
.repair-area{left:0;top:1457px;width:1200px;height:665px;background:#fbfbfb}
.intro{left:230px;top:1494px;width:740px;text-align:center;font-size:11px;line-height:1.5;color:#333}
.repair{width:182px;height:260px;text-align:center}
.repair svg{display:block;margin:28px auto 0}
.repair h6{margin-top:14px;font:400 17px "Roboto",sans-serif;color:#333;line-height:1.2;height:44px}
.repair p{margin:18px 20px 0;font-size:10px;line-height:1.45;color:#999}
.repair hr{width:40px;margin:22px auto 0;border:0;border-top:3px solid #555}
.repair.active{color:#fff}
.repair.active h6,.repair.active p{color:#333}
.repair.active p{color:#fff}
.repair.active h6{color:#333}
.repair.active hr{border-top-color:#fff}

/* services trio */
.service{top:2122px;width:400px;height:225px;color:#fff}
.service h4{position:absolute;left:120px;top:46px;font:400 29px "Roboto",sans-serif;line-height:1.15}
.service p{position:absolute;left:120px;top:138px;width:210px;font-size:11.5px;line-height:1.4}
.service svg{position:absolute;left:36px;top:58px}

/* why choose */
.title{left:0;width:1200px;text-align:center;font:400 36px "Roboto",sans-serif;color:#222}
.slider{left:0;top:2437px;width:1200px;height:225px}
.slide{top:0;height:187px}
.caption-bar{left:0;top:2624px;width:1200px;height:38px;background:rgba(20,20,20,.85)}
.caption-bar span{position:absolute;top:10px;color:#fff;font-size:14px}
.arrow{width:38px;height:38px;border-radius:50%;background:#222;top:2530px;display:flex;align-items:center;justify-content:center}

/* testimonials */
.stars{left:518px;top:2738px;display:flex;gap:4px}
.reviews{left:0;top:2783px;width:1200px;height:340px;background:var(--grey-bg)}
.review{top:2810px;width:205px}
.review h5{font:400 18px "Roboto",sans-serif;color:var(--orange)}
.review .tag{margin-top:8px;font-size:10px;color:#333;display:flex;align-items:center;gap:6px}
.review .tag i{width:9px;height:9px;border-radius:50%;background:var(--orange)}
.review .quote{position:relative;margin-top:24px;background:#e2e2e2;padding:12px 10px;font-size:10.5px;line-height:1.4;color:#444;height:150px}
.review .quote:after{content:"";position:absolute;right:20px;bottom:-12px;border-left:12px solid transparent;border-top:12px solid #e2e2e2}
.review .name{margin-top:24px;text-align:center;font-size:11px;color:#333}
.rev-arrow{top:2955px;color:#888;font-size:22px}

/* footer */
.footer{left:0;top:3127px;width:1200px;height:502px;background:var(--footer)}
.footer h4{position:absolute;font:400 18px "Roboto",sans-serif;color:#fff}
.info-list{left:168px;top:3196px;list-style:none;font-size:12px;color:#ddd;line-height:2.1}
.info-list li:before{content:"";display:inline-block;width:4px;height:4px;background:#ddd;border-radius:50%;margin-right:6px;vertical-align:middle}
.post{left:392px;width:380px}
.post .date{position:absolute;left:0;top:0;width:42px;height:38px;background:var(--orange);color:#fff;font-size:8px;text-align:center;padding-top:6px;line-height:1.3}
.post .body{position:absolute;left:62px;top:0;width:320px}
.post h6{font:700 13px "Roboto",sans-serif;color:#fff}
.post p{margin-top:4px;font-size:10px;line-height:1.4;color:#ccc}
.post .read{display:inline-flex;margin-top:8px;height:20px;padding:0 10px;background:#fff;border-radius:10px;font-size:10px;color:#333;align-items:center;gap:4px}
.post .read i{width:6px;height:6px;border-radius:50%;background:#333}
.timeline{left:414px;top:3190px;width:2px;height:180px;background:#8a96a2}
.news-input{left:838px;top:3197px;width:200px;height:42px;background:#ddd;font-size:11px;color:#888;padding:13px 10px}
.subscribe{left:838px;top:3255px;width:98px;height:30px;background:var(--orange);color:#fff;font:700 11px "Roboto",sans-serif;display:flex;align-items:center;justify-content:center}
.f-social{left:838px;top:3312px;display:flex;gap:8px}
.f-social span{width:25px;height:25px;border-radius:50%;background:#7c8894}
.contact{top:3497px;height:66px;border:1px solid var(--footer-line);display:flex;gap:12px;padding:8px 10px}
.contact b{flex:none;width:30px;height:30px;background:var(--orange);border-radius:3px;display:flex;align-items:center;justify-content:center;margin-top:6px}
.contact h6{font:400 14px "Roboto",sans-serif;color:var(--orange)}
.contact p{font-size:10px;color:#ddd;line-height:1.4;margin-top:2px}
.contact u{font-size:10px;color:var(--orange)}
.copyright{left:0;top:3598px;width:1200px;height:31px;text-align:center;font-size:10px;color:#ccc;border-top:1px solid var(--footer-line);padding-top:10px;position:absolute}
</style>
</head>
<body>

<!-- top bar -->
<div class="abs topbar">
  <div class="abs quick-links">QUICK LINKS <i></i></div>
  <div class="abs lang">Gre | Eng</div>
  <div class="abs social"><span></span><span></span><span></span><span></span><span></span><span></span><span></span><span></span></div>
</div>

<!-- header -->
<header class="abs header">
  <div class="abs brand"><span></span>Fixoloda</div>
  <nav class="abs nav"><a>Repairs</a><a>20 Stores</a><a>Blog</a></nav>
  <div class="abs call">
    <svg width="34" height="30" viewBox="0 0 34 30"><path d="M3 10c0-5 28-5 28 0v3h-7v-3H10v3H3z" fill="#f07d1c"/><path d="M8 14h18l4 14H4z" fill="#f07d1c"/><circle cx="17" cy="21" r="4" fill="#fff"/></svg>
    <div><small>Call to Us</small><strong>210 555 0142</strong></div>
  </div>
  <div class="abs livechat">Live Chat</div>
</header>

<!-- hero -->
<div class="photo hero" role="img" aria-label="Video still of technicians repairing devices at workbenches">
  <svg class="abs play" width="70" height="70" viewBox="0 0 70 70"><circle cx="35" cy="35" r="31" fill="rgba(255,255,255,.12)" stroke="#fff" stroke-width="3"/><path d="M28 21l20 14-20 14z" fill="#fff"/></svg>
</div>
<div class="abs result-band">
  <h2>Repairs Complete with happy Customers.</h2>
  <p>Yep, we fix a lot of devices!</p>
</div>
<div class="abs counter"><span>1</span><span>4</span><span>5</span><span>3</span></div>
<div class="abs counter-label">
  <svg width="236" height="50" viewBox="0 0 236 50"><path d="M0 0h236v28l-118 22L0 28z" fill="#fff"/></svg>
  <div>COUNTE REPAIRS</div>
</div>

<!-- promo panels -->
<div class="photo locations" role="img" aria-label="Grey close-up of a circuit board behind the store locator">
  <h3>20 fixoloda Locations</h3>
  <div class="find-btn">
    <b><svg width="22" height="30" viewBox="0 0 22 30"><path d="M11 0C5 0 0 5 0 11c0 8 11 19 11 19s11-11 11-19C22 5 17 0 11 0z" fill="#fff"/><circle cx="11" cy="11" r="4" fill="#f07d1c"/></svg></b>
    <span>Find a store near You</span>
  </div>
  <div class="view-map"><i></i>View Map</div>
</div>
<div class="photo match" role="img" aria-label="Repair shop interior with a technician at a counter">
  <h3>FIND A LOWER PRICE FOR YOUR</h3>
  <h4>Aerophone or Aeropad repair?*</h4>
  <div class="match-box">WE WILL MATCH IT!*</div>
  <small>* Terms and conditions apply, click to read more</small>
</div>

<!-- features -->
<div class="abs feature" style="left:160px">
  <div class="photo" role="img" aria-label="Hands soldering a circuit board" style="background:linear-gradient(135deg,#b84a2a,#e7c9a8)"></div>
  <h5>Open Service Area</h5>
  <p>Repair right in front of you<br>No closed doors, no back rooms</p>
  <div class="btn-more"><i></i>Read More</div>
</div>
<div class="abs feature" style="left:382px">
  <div class="photo" role="img" aria-label="Technician working on a motherboard" style="background:linear-gradient(135deg,#5a6b78,#c2b8ab)"></div>
  <h5>Save 50-75% on multiple repairs</h5>
  <p>If your device needs more than 1 part replaced, save up to 75% on addition parts.</p>
  <div class="btn-more"><i></i>Read More</div>
</div>
<div class="abs feature" style="left:605px">
  <div class="photo" role="img" aria-label="Hand holding a phone in a shop" style="background:linear-gradient(135deg,#c86d3c,#f0d2c0)"></div>
  <h5>Accessories</h5>
  <p>Lorem Ipsum is simply dummy text of the printing and typesetting industry.</p>
  <div class="btn-more"><i></i>Read More</div>
</div>
<div class="abs feature" style="left:825px">
  <div class="photo" role="img" aria-label="Opened laptop with tools on a desk" style="background:linear-gradient(135deg,#4b4b4b,#a8a8a8)"></div>
  <h5>20 minute repairs</h5>
  <p>Most repairs can be completed in about 20 minutes.</p>
  <div class="btn-more"><i></i>Read More</div>
</div>

<!-- what we repair -->
<div class="abs section-band">What we repair?</div>
<div class="abs repair-area"></div>
<p class="abs intro">Lorem Ipsum is simply dummy text of the printing and typesetting industry. Lorem Ipsum has been the industry's standard dummy text ever since the 1500s, when an unknown printer took a galley.</p>

<svg class="abs" style="left:526px;top:1560px" width="182" height="255" viewBox="0 0 182 255"><path d="M0 22L91 0l91 22v233H0z" fill="#f49a3c"/></svg>

<div class="abs repair" style="left:157px;top:1560px">
  <svg width="30" height="54" viewBox="0 0 30 54"><rect x="2" y="2" width="26" height="50" rx="4" fill="none" stroke="#111" stroke-width="3"/><rect x="6" y="9" width="18" height="32" fill="#111"/></svg>
  <h6>Aerophone Repair</h6><p>Lorem Ipsum is simply dummy text of the printing and typesetting industry.</p><hr>
</div>
<div class="abs repair" style="left:341px;top:1560px">
  <svg width="44" height="56" viewBox="0 0 44 56"><rect x="2" y="2" width="40" height="52" rx="4" fill="none" stroke="#111" stroke-width="3"/><rect x="7" y="8" width="30" height="38" fill="none" stroke="#111" stroke-width="2"/></svg>
  <h6>Aeropad Repair</h6><p>Lorem Ipsum is simply dummy text of the printing and typesetting industry.</p><hr>
</div>
<div class="abs repair active" style="left:526px;top:1560px">
  <svg width="30" height="54" viewBox="0 0 30 54"><rect x="2" y="2" width="26" height="50" rx="4" fill="none" stroke="#111" stroke-width="3"/><rect x="6" y="9" width="18" height="32" fill="#111"/></svg>
  <h6>Aeropod Touch Repair</h6><p>Lorem Ipsum is simply dummy text of the printing and typesetting industry.</p><hr>
</div>
<div class="abs repair" style="left:708px;top:1560px">
  <svg width="30" height="54" viewBox="0 0 30 54"><rect x="2" y="2" width="26" height="50" rx="5" fill="none" stroke="#111" stroke-width="3"/><rect x="6" y="10" width="18" height="30" fill="none" stroke="#111" stroke-width="2"/></svg>
  <h6>Sorvan Repair</h6><p>Lorem Ipsum is simply dummy text of the printing and typesetting industry.</p><hr>
</div>
<div class="abs repair" style="left:890px;top:1560px">
  <svg width="32" height="54" viewBox="0 0 32 54"><rect x="2" y="2" width="28" height="50" rx="5" fill="none" stroke="#111" stroke-width="3"/><rect x="7" y="8" width="18" height="16" fill="#111"/><g fill="#111"><rect x="7" y="30" width="4" height="3"/><rect x="14" y="30" width="4" height="3"/><rect x="21" y="30" width="4" height="3"/><rect x="7" y="37" width="4" height="3"/><rect x="14" y="37" width="4" height="3"/><rect x="21" y="37" width="4" height="3"/></g></svg>
  <h6>Bramble Repair</h6><p>Lorem Ipsum is simply dummy text of the printing and typesetting industry.</p><hr>
</div>

<div class="abs repair" style="left:157px;top:1840px">
  <svg width="64" height="54" viewBox="0 0 64 54"><rect x="2" y="2" width="60" height="38" fill="#111"/><path d="M26 40h12l3 10H23z" fill="#111"/><rect x="18" y="49" width="28" height="3" fill="#111"/></svg>
  <h6>Aerodesk Repairs</h6><p>Lorem Ipsum is simply dummy text of the printing and typesetting industry.</p><hr>
</div>
<div class="abs repair" style="left:341px;top:1840px">
  <svg width="70" height="54" viewBox="0 0 70 54"><rect x="10" y="8" width="50" height="34" rx="2" fill="none" stroke="#111" stroke-width="3"/><path d="M2 44h66l-4 6H6z" fill="#111"/></svg>
  <h6>Aerobook Repair</h6><p>Lorem Ipsum is simply dummy text of the printing and typesetting industry.</p><hr>
</div>
<div class="abs repair" style="left:526px;top:1840px">
  <svg width="70" height="54" viewBox="0 0 70 54"><rect x="2" y="6" width="44" height="32" fill="none" stroke="#111" stroke-width="3"/><rect x="18" y="40" width="12" height="6" fill="#111"/><rect x="12" y="46" width="24" height="3" fill="#111"/><rect x="52" y="4" width="16" height="46" fill="#111"/></svg>
  <h6>Computer Repair</h6><p>Lorem Ipsum is simply dummy text of the printing and typesetting industry.</p><hr>
</div>
<div class="abs repair" style="left:708px;top:1840px">
  <svg width="70" height="54" viewBox="0 0 70 54"><rect x="10" y="8" width="50" height="34" rx="2" fill="none" stroke="#111" stroke-width="3"/><path d="M2 44h66l-4 6H6z" fill="#111"/></svg>
  <h6>Laptop Repair</h6><p>Lorem Ipsum is simply dummy text of the printing and typesetting industry.</p><hr>
</div>
<div class="abs repair" style="left:890px;top:1840px">
  <svg width="54" height="54" viewBox="0 0 54 54"><circle cx="27" cy="24" r="12" fill="#111"/><rect x="21" y="36" width="12" height="8" fill="#111"/><rect x="23" y="46" width="8" height="3" fill="#111"/><g stroke="#111" stroke-width="3"><path d="M27 2v6M5 24h6M43 24h6M11 8l5 5M43 8l-5 5"/></g></svg>
  <h6>Business Services</h6><p>Lorem Ipsum is simply dummy text of the printing and typesetting industry.</p><hr>
</div>

<!-- services trio -->
<div class="abs service" style="left:0;background:var(--orange)">
  <svg width="66" height="40" viewBox="0 0 66 40"><path d="M0 4h40v26H0zM42 12h14l10 10v8H42z" fill="#fff"/><circle cx="14" cy="33" r="6" fill="#fff" stroke="#f07d1c" stroke-width="3"/><circle cx="52" cy="33" r="6" fill="#fff" stroke="#f07d1c" stroke-width="3"/></svg>
  <h4>Find A store<br>near you?</h4>
  <p>Lorem Ipsum is simply dummy text of the printing and typesetting industry. Lorem Ipsum has been the industry's...</p>
</div>
<div class="abs service" style="left:400px;background:var(--orange-light)">
  <svg width="50" height="60" viewBox="0 0 50 60" style="left:50px;top:50px"><path d="M4 16h42l-4 44H8z" fill="#fff"/><path d="M15 20v-8a10 10 0 0 1 20 0v8" fill="none" stroke="#fff" stroke-width="4"/></svg>
  <h4>Send us your<br>device</h4>
  <p>Lorem Ipsum is simply dummy text of the printing and typesetting industry.</p>
</div>
<div class="abs service" style="left:800px;background:var(--orange-dark)">
  <svg width="56" height="56" viewBox="0 0 56 56" style="left:10px;top:52px"><circle cx="28" cy="28" r="25" fill="none" stroke="#fff" stroke-width="4"/><text x="28" y="40" text-anchor="middle" font-family="Roboto,sans-serif" font-weight="700" font-size="32" fill="#fff">$</text></svg>
  <h4 style="left:84px">Free pickup in<br>Athens</h4>
  <p style="left:84px">Lorem Ipsum is simply dummy text of the printing and typesetting industry.</p>
</div>

<!-- why choose -->
<div class="abs title" style="top:2375px">Why choose fixoloda?</div>
<div class="abs slider">
  <div class="photo slide" style="left:0;width:250px;background:linear-gradient(135deg,#2f5c8a,#c09a7a)" role="img" aria-label="Hands working inside an open computer"></div>
  <div class="photo slide" style="left:250px;width:265px;background:linear-gradient(135deg,#a84432,#e2cbb1)" role="img" aria-label="Soldering a circuit board"></div>
  <div class="photo slide" style="left:515px;width:265px;background:linear-gradient(135deg,#c8775a,#f1dccf)" role="img" aria-label="Phone held up in a store"></div>
  <div class="photo slide" style="left:780px;width:265px;background:linear-gradient(135deg,#3a3a3a,#9d9d9d)" role="img" aria-label="Laptop being repaired"></div>
  <div class="photo slide" style="left:1045px;width:155px;background:linear-gradient(135deg,#6c5a4a,#c4b2a0)" role="img" aria-label="Repair tools on a bench"></div>
</div>
<div class="abs caption-bar">
  <span style="left:66px">Open Service Area ›</span>
  <span style="left:268px">Save 50-75% on multiple repairs ›</span>
  <span style="left:542px">Accessories ›</span>
  <span style="left:842px">20 minute repairs ›</span>
</div>
<div class="abs arrow" style="left:34px"><svg width="12" height="14"><path d="M9 1L3 7l6 6" stroke="#fff" stroke-width="2" fill="none"/></svg></div>
<div class="abs arrow" style="left:1116px"><svg width="12" height="14"><path d="M3 1l6 6-6 6" stroke="#fff" stroke-width="2" fill="none"/></svg></div>

<!-- testimonials -->
<div class="abs title" style="top:2686px">What our customer saying</div>
<div class="abs stars">
  <svg width="160" height="30" viewBox="0 0 160 30"><defs><path id="st" d="M15 1l4.3 9 9.7 1.2-7.1 6.7 1.9 9.7L15 22.8 6.2 27.6l1.9-9.7L1 11.2 10.7 10z" fill="#f3b527"/></defs><use href="#st"/><use href="#st" x="32"/><use href="#st" x="64"/><use href="#st" x="96"/><use href="#st" x="128"/></svg>
</div>
<div class="abs reviews"></div>
<div class="abs rev-arrow" style="left:128px">‹</div>
<div class="abs rev-arrow" style="left:1046px">›</div>
<div class="abs review" style="left:160px"><h5>Laptop Repair</h5><div class="tag"><i></i>Overheating</div><div class="quote">Lorem Ipsum is simply dummy text of the printing and typesetting industry. Lorem Ipsum has been the industry's standard dummy text ever since the 1500s, when an unknown printer took a galley of type and scrambled it to make a type specimen book.</div><div class="name">Elena P.Marousi</div></div>
<div class="abs review" style="left:382px"><h5>Laptop Repair</h5><div class="tag"><i></i>Overheating</div><div class="quote">Lorem Ipsum is simply dummy text of the printing and typesetting industry. Lorem Ipsum has been the industry's standard dummy text ever since the 1500s, when an unknown printer took a galley of type and scrambled it to make a type specimen book.</div><div class="name">Elena P.Marousi</div></div>
<div class="abs review" style="left:605px"><h5>Laptop Repair</h5><div class="tag"><i></i>Overheating</div><div class="quote">Lorem Ipsum is simply dummy text of the printing and typesetting industry. Lorem Ipsum has been the industry's standard dummy text ever since the 1500s, when an unknown printer took a galley of type and scrambled it to make a type specimen book.</div><div class="name">Elena P.Marousi</div></div>
<div class="abs review" style="left:825px"><h5>Laptop Repair</h5><div class="tag"><i></i>Overheating</div><div class="quote">Lorem Ipsum is simply dummy text of the printing and typesetting industry. Lorem Ipsum has been the industry's standard dummy text ever since the 1500s, when an unknown printer took a galley of type and scrambled it to make a type specimen book.</div><div class="name">Elena P.Marousi</div></div>

<!-- footer -->
<footer class="abs footer"></footer>
<h4 class="abs" style="left:160px;top:3158px;font:400 18px Roboto,sans-serif;color:#fff">Information</h4>
<ul class="abs info-list"><li>Repairs</li><li>20 Stores</li><li>Blog</li></ul>
<h4 class="abs" style="left:392px;top:3158px;font:400 18px Roboto,sans-serif;color:#fff">Fixoloda Blog</h4>
<div class="abs timeline"></div>
<div class="abs post" style="top:3196px"><div class="date">26 OCT<br>2017</div><div class="body"><h6>Lorem Ipsum is simply dummy text...</h6><p>Lorem Ipsum is simply dummy text of the printing and typesetting industry. Lorem Ipsum has been the industry's...</p><span class="read"><i></i>Read More...</span></div></div>
<div class="abs post" style="top:3302px"><div class="date">26 OCT<br>2017</div><div class="body"><h6>Lorem Ipsum is simply dummy text...</h6><p>Lorem Ipsum is simply dummy text of the printing and typesetting industry. Lorem Ipsum has been the industry's...</p><span class="read"><i></i>Read More...</span></div></div>
<h4 class="abs" style="left:838px;top:3158px;font:400 18px Roboto,sans-serif;color:#fff">newsletter</h4>
<div class="abs news-input">Enter Your Email id</div>
<div class="abs subscribe">SUBSCRIBE</div>
<div class="abs f-social"><span></span><span></span><span></span><span></span></div>

<div class="abs" style="left:160px;top:3426px;font:400 18px Roboto,sans-serif;color:#fff">Can't find what you need?</div>
<div class="abs contact" style="left:160px;width:272px">
  <b><svg width="18" height="14" viewBox="0 0 18 14"><rect x="1" y="1" width="16" height="12" fill="none" stroke="#fff" stroke-width="2"/><path d="M1 1l8 7 8-7" fill="none" stroke="#fff" stroke-width="2"/></svg></b>
  <div><h6>Email Support</h6><p>We usually responded within 24 hours</p><u>Click to send email</u></div>
</div>
<div class="abs contact" style="left:466px;width:272px">
  <b><svg width="16" height="16" viewBox="0 0 16 16"><path d="M3 1l3 3-2 2c1 2 3 4 6 6l2-2 3 3-2 2C7 15 1 9 1 3z" fill="#fff"/></svg></b>
  <div><h6>Contact our call center</h6><p>Call to speak to a customer service rep.</p><u>210 555 0142</u></div>
</div>
<div class="abs contact" style="left:766px;width:274px">
  <b><svg width="18" height="16" viewBox="0 0 18 16"><path d="M1 1h16v10H7l-4 4v-4H1z" fill="#fff"/></svg></b>
  <div><h6>Live chat</h6><p>Chat with an Fixoloda technician now.</p><u>Click to chat</u></div>
</div>
<div class="copyright">Copyright 2017. All Right Reserved.</div>

</body>
</html>
```